Water Filtration Company needs a business card design using our existing logo/colours!

We design and manufacture and export specialised water filtration equipment. Our equipment will take unclean dirty water and filters to safe clean drinkable water.
We would like to see designs using our existing logo and colours (see attached "Palette") that represents clean safe drinking water (fresh, clean designs but still professional and modern). Our customers are other businesses who supply water filtration equipment, governments, and private individuals.
BUSINESS CARD DETAILS (Common details):
Tel: + 61 7 55 419 276
www: brindlepeak.com.au
Address: 3/47 Cordwell Parade
Marlow Flats NSW 2593 Australia
(please include the word Australia as we are an international company)
Must include: COMMERCIAL WATER FILTRATION EQUIPMENT
NAME NO 1:
Owen Pritch
General Manager
Mobile: +61 427 38 91 04
Email: owen@brindlepeak.com.au
NAME NO. 2:
Gina Rosk
Business Manager
Mobile: +61 409 572 148
Email: gina@brindlepeak.com.au
Must Have:
1) PRINT READY IN .AI & .PDF FORMATS
2) Also saved in file format .ai (Adobe Illustrator - compatible with CS4)
3) Use existing LOGO & COLOURS: Please use our logo (see attached file)
4) FONTS: we have used Avenir & Helvetica in the past but are open to other font types for the address etc.
Thank you!

```html
<!DOCTYPE html>
<html lang="en">
<head>
<meta charset="utf-8">
<title>Brindle Peak – Business Cards</title>
<link rel="stylesheet" href="https://fonts.googleapis.com/css2?family=Arimo:wght@400;700&display=swap">
<style>
  :root {
    --frame: #262626;
    --panel: #8c8c8c;
    --card: #ffffff;
    --ink: #2a2a2a;
    --teal: #1797b8;
    --teal-deep: #0d5f86;
    --logo: #1f6f95;
    --rule: #3a3a3a;
    --label-blue: #1b6a98;
    --label-light: #ffffff;
  }
  * { box-sizing: border-box; margin: 0; padding: 0; }
  html, body { width: 1200px; height: 1000px; overflow: hidden; background: var(--frame); }
  body { position: relative; font-family: "Arimo", Helvetica, Arial, sans-serif; }

  .panel { position: absolute; background: var(--panel); overflow: hidden; }
  .panel--main { left: 16px; top: 16px; width: 1168px; height: 584px; }
  .panel--front { left: 16px; top: 608px; width: 582px; height: 376px; }
  .panel--alt { left: 604px; top: 608px; width: 580px; height: 376px; }

  .panel-label { position: absolute; font-weight: 700; font-size: 20px; letter-spacing: 0.3px; }
  .panel--main .panel-label { right: 14px; top: 12px; color: var(--label-blue); }
  .panel--front .panel-label { left: 10px; top: 10px; color: var(--label-light); }
  .panel--alt .panel-label { right: 12px; bottom: 8px; color: var(--label-light); }

  .card {
    position: absolute; width: 38.75em; height: 23.6em;
    left: 50%; top: 50%; transform: translate(-50%, -50%);
    background: var(--card); box-shadow: 0 0.6em 1.4em rgba(0,0,0,0.35);
    color: var(--ink);
  }
  .panel--main .card { font-size: 16px; }
  .panel--front .card, .panel--alt .card { font-size: 9.6px; }

  .brand {
    position: absolute; left: 2.4em; top: 2.6em;
    display: flex; align-items: center; gap: 0.5em;
    font-size: 2.6em; font-weight: 700; color: var(--logo); letter-spacing: -0.02em;
  }
  .brand-dot { width: 0.55em; height: 0.55em; border-radius: 50%; background: var(--teal); }

  .person { position: absolute; right: 2.4em; top: 3em; width: 17em; text-align: right; }
  .person-name { font-size: 1.7em; color: var(--ink); padding-bottom: 0.15em; }
  .person-rule { height: 1px; background: var(--rule); margin-right: -1em; }
  .person-role { font-size: 0.95em; color: var(--teal); margin-top: 0.3em; }

  .contact-rule { position: absolute; left: 1.6em; top: 12.4em; width: 19em; height: 1px; background: var(--rule); }
  .contacts { position: absolute; left: 2.4em; top: 13.3em; list-style: none; font-size: 1em; line-height: 1.3; }
  .contacts li { display: flex; align-items: center; gap: 0.7em; }
  .contacts li.gap { margin-top: 0.5em; }
  .contacts svg { width: 1em; height: 1em; flex: none; fill: var(--teal-deep); }
  .contacts .indent { padding-left: 1.7em; }

  .card--front {
    background: linear-gradient(120deg, var(--teal) 0%, #1287ab 45%, var(--teal-deep) 100%);
    display: flex; align-items: center; justify-content: center; gap: 0.6em;
  }
  .front-name { font-size: 4.6em; font-weight: 700; color: #fff; letter-spacing: -0.02em; }
  .front-dot { width: 2em; height: 2em; border-radius: 50%; background: #fff; }
</style>
</head>
<body>

<svg width="0" height="0" style="position:absolute" aria-hidden="true">
  <defs>
    <symbol id="icon-mobile" viewBox="0 0 16 16"><path d="M4 1h8v14H4z M5.5 2.5v9h5v-9z M7 12.5h2v1.2H7z" fill-rule="evenodd"/></symbol>
    <symbol id="icon-phone" viewBox="0 0 16 16"><path d="M2 6c0-2 3-3 6-3s6 1 6 3v1.5h-3V6H5v1.5H2z M4 8h8l1.5 5h-11z"/></symbol>
    <symbol id="icon-mail" viewBox="0 0 16 16"><path d="M1 3.5h14v9H1z M2.5 4.8 8 9l5.5-4.2" fill-rule="evenodd"/><path d="M2 4.5 8 9l6-4.5" stroke="#fff" stroke-width="1.2" fill="none"/></symbol>
    <symbol id="icon-globe" viewBox="0 0 16 16"><circle cx="8" cy="8" r="7"/><path d="M1 8h14M8 1v14M8 1c-3 3-3 11 0 14M8 1c3 3 3 11 0 14" stroke="#fff" stroke-width="1" fill="none"/></symbol>
    <symbol id="icon-pin" viewBox="0 0 16 16"><path d="M8 1a5 5 0 0 1 5 5c0 4-5 9-5 9S3 10 3 6a5 5 0 0 1 5-5z"/><circle cx="8" cy="6" r="2" fill="#fff"/></symbol>
  </defs>
</svg>

<section class="panel panel--main">
  <div class="panel-label">Owen Pritch (BACK)</div>
  <article class="card card--back">
    <div class="brand"><span class="brand-dot"></span>Brindle Peak</div>
    <div class="person">
      <div class="person-name">Owen Pritch</div>
      <div class="person-rule"></div>
      <div class="person-role">General Manager</div>
    </div>
    <div class="contact-rule"></div>
    <ul class="contacts">
      <li><svg><use href="#icon-mobile"/></svg>+61 427 38 91 04</li>
      <li><svg><use href="#icon-phone"/></svg>+ 61 7 55 419 276</li>
      <li><svg><use href="#icon-mail"/></svg>owen@brindlepeak.com.au</li>
      <li><svg><use href="#icon-globe"/></svg>www: brindlepeak.com.au</li>
      <li class="gap"><svg><use href="#icon-pin"/></svg>Address: 3/47 Cordwell Parade</li>
      <li class="indent">Marlow Flats NSW 2593 Australia</li>
    </ul>
  </article>
</section>

<section class="panel panel--front">
  <div class="panel-label">FRONT</div>
  <article class="card card--front">
    <span class="front-dot"></span><span class="front-name">Brindle Peak</span>
  </article>
</section>

<section class="panel panel--alt">
  <article class="card card--back">
    <div class="brand"><span class="brand-dot"></span>Brindle Peak</div>
    <div class="person">
      <div class="person-name">Gina Rosk</div>
      <div class="person-rule"></div>
      <div class="person-role">Business Manager</div>
    </div>
    <div class="contact-rule"></div>
    <ul class="contacts">
      <li><svg><use href="#icon-mobile"/></svg>+61 409 572 148</li>
      <li><svg><use href="#icon-phone"/></svg>+ 61 7 55 419 276</li>
      <li><svg><use href="#icon-mail"/></svg>gina@brindlepeak.com.au</li>
      <li><svg><use href="#icon-globe"/></svg>www: brindlepeak.com.au</li>
      <li class="gap"><svg><use href="#icon-pin"/></svg>Address: 3/47 Cordwell Parade</li>
      <li class="indent">Marlow Flats NSW 2593 Australia</li>
    </ul>
  </article>
  <div class="panel-label">Gina Rosk (BACK)</div>
</section>

</body>
</html>
```